Orbell Consulting- executive coaching business

looking for business card design for a newly started coaching business.
specialising in Exective coaching, Leadership, NLP and Motivation.
Looking for a simple, classy design using the existing logo attached and colour themes that complement the logo.
No red or orange in the business card design please.

Target Market(s)

Defence and Veteran community

Industry/Entity Type

Life Coaching

Contact Information for Business Card

looking for business cards for newly started coaching business.
specialising in Exective Coaching, Leadership, NLP and Motivation

Font styles to use
Serif
Script

Colors
0556a4
3176b5
86cfc6
33b8a4

Requirements
Must have
• Logo
• Email address- Jess@orbellconsulting.com.au
• Contact number
• Services provided - Executive Coaching, Leadership, NLP and Motivational Mapping.
Nice to have
• Same colours as logo
Should not have
• Red or orange

```html
<!DOCTYPE html>
<html lang="en">
<head>
<meta charset="utf-8">
<title>Orbell Consulting – Business Cards</title>
<link href="https://fonts.googleapis.com/css2?family=Montserrat:wght@700&family=Roboto:wght@400;500&family=Pacifico&display=swap" rel="stylesheet">
<style>
  :root{
    --page:#e7e3dd;
    --card-white:#ffffff;
    --card-black:#050505;
    --ink:#111111;
    --light:#f4f4f4;
    --faint-on-white:#e2e2e2;
    --faint-on-black:#1c1c1c;
    --faint-text:#2a2a2a;
  }
  *{margin:0;padding:0;box-sizing:border-box}
  html,body{width:1200px;height:892px;overflow:hidden;background:var(--page)}
  .canvas{position:relative;width:1200px;height:892px}
  .card{position:absolute;top:303px;width:500px;height:286px;overflow:hidden;
        box-shadow:0 6px 18px rgba(0,0,0,.25)}
  .card--front{left:70px;background:var(--card-white)}
  .card--back{left:630px;background:var(--card-black)}

  .front-art{position:absolute;inset:0}
  .brand{position:absolute;left:26px;top:40px;display:flex;align-items:center;gap:12px}
  .brand__dot{width:58px;height:58px;border:2px solid var(--ink);border-radius:50%}
  .brand__name{font-family:"Montserrat",sans-serif;font-weight:700;font-size:25px;
               color:var(--ink);letter-spacing:.5px;text-transform:uppercase}

  .contact{position:absolute;left:28px;top:192px;color:var(--light);
           font-family:"Roboto",sans-serif}
  .contact__name{font-size:24px;font-weight:500;margin-bottom:12px}
  .contact__row{display:flex;align-items:center;gap:9px;font-size:16px;line-height:24px}
  .contact__icon{width:12px;height:12px;background:var(--light);display:flex;
                 align-items:center;justify-content:center}

  .back-mark{position:absolute;left:30px;top:40px;width:200px;height:200px;
             border:16px solid var(--faint-on-black);border-radius:50%}
  .back-brand{position:absolute;left:40px;top:196px;font-family:"Montserrat",sans-serif;
              font-weight:700;font-size:22px;color:var(--faint-text);text-transform:uppercase}
  .services{position:absolute;right:30px;top:58px;text-align:right;color:var(--light)}
  .services__title{font-family:"Pacifico",cursive;font-size:28px;margin-bottom:14px}
  .services__list{list-style:none;font-family:"Roboto",sans-serif;font-size:17px;line-height:27px}
</style>
</head>
<body>
<main class="canvas">

  <section class="card card--front" aria-label="Business card front">
    <svg class="front-art" width="500" height="286" viewBox="0 0 500 286" aria-hidden="true">
      <rect x="0" y="172" width="500" height="114" fill="var(--card-black)"/>
      <circle cx="405" cy="75" r="160" fill="var(--card-white)"/>
      <circle cx="405" cy="85" r="120" fill="none" stroke="var(--faint-on-white)" stroke-width="6"/>
    </svg>

    <div class="brand">
      <span class="brand__dot"></span>
      <span class="brand__name">Orbell Consulting</span>
    </div>

    <div class="contact">
      <p class="contact__name">Daniel Hartley</p>
      <p class="contact__row">
        <span class="contact__icon">
          <svg width="8" height="8" viewBox="0 0 8 8"><path d="M1 1h2l1 2-1 1a4 4 0 0 0 1 1l1-1 2 1v2h-1A6 6 0 0 1 1 2z" fill="var(--card-black)"/></svg>
        </span>
        021 5603 7714
      </p>
      <p class="contact__row">
        <span class="contact__icon">
          <svg width="8" height="8" viewBox="0 0 8 8"><rect x="0.5" y="1.5" width="7" height="5" fill="none" stroke="var(--card-black)"/><path d="M.5 1.5 4 4.5l3.5-3" fill="none" stroke="var(--card-black)"/></svg>
        </span>
        Jess@orbellconsulting.com.au
      </p>
    </div>
  </section>

  <section class="card card--back" aria-label="Business card back">
    <div class="back-mark"></div>
    <p class="back-brand">Orbell Consulting</p>
    <div class="services">
      <h2 class="services__title">Services provided</h2>
      <ul class="services__list">
        <li>Leadership</li>
        <li>Executive Coaching</li>
        <li>NLP and Motivational Mapping</li>
      </ul>
    </div>
  </section>

</main>
</body>
</html>
```